Contact card for an aggressive entrepreneur

I am looking for a business/contact card as an individual. I operate under the company name The Varlow Circle, LLC (but don't generally use that other than for billing). I have explored a few ideas and am now turning to makerhive to connect with people more creative than me. I am trying to capture a diverse set of passions, which I will summarize with the following keywords (which may or may not be ON the card and are in no particular order):

entrepreneur
shark diver
MBA
visionary
defenseman
marketing guru
hockey coach
teacher
reader
writer
cook
captain
scuba diver
beach bum
Type A
Columbia
Vermont
New York
Montauk
founder
leader
focused
driven
teammate father

hope that makes some sense!
Updates

Please note the photo is for reference - unless there is a really creative way to use it I do not need a card with a head shot (I am not a model or an actor!)

Project Deadline Extended
Reason: There have been several requests to submit designs so we will close this project this Wednesday and select a design by this Friday. Thank you to all for your great ideas and submissions!

I am reviewing the designs and will select one by end of day tomorrow, Tuesday, EST
Thank you to all who participated!

Target Market(s)

everyone from business contacts to personal acquaintances

Industry/Entity Type

Business

Requirements
Must have
• Must be utterly original, extraordinary and memorable.
How it achieves that is up to you!
Essential contact information that needs to be included:

phone: (917) 555-4173
email: tomas@varlowcircle.example
skype: tomas.varlow
Nice to have
• A striking visual whether that is a photo or illustration
Some way of conveying the diversity of what I am and what I do
Feel free to use the printing or physical material of the card to make it stand out.
Should not have
• I am not into "logos" but that being said I do not want to limit creativity in any way so feel free to ignore any part of this brief if you disagree with me. No need to use the attached photo of me, but that's what I look like.

```html
<!DOCTYPE html>
<html lang="en">
<head>
<meta charset="utf-8">
<title>Tomas Varlow — Contact Card</title>
<link rel="stylesheet" href="https://fonts.googleapis.com/css2?family=Open+Sans:wght@400;700&family=Roboto:wght@300;400&family=Roboto+Condensed:wght@300&display=swap">
<style>
  :root {
    --paper: #ffffff;
    --ink: #111111;
    --swoosh-red: #ee1c1c;
    --swoosh-yellow: #fbbf1a;
    --wave: #8a8a8a;
    --portrait-top: #b8a27a;
    --portrait-mid: #5a5448;
    --portrait-bottom: #2a2a2c;
  }
  html, body {
    margin: 0;
    padding: 0;
    width: 1200px;
    height: 848px;
    overflow: hidden;
    background: var(--paper);
  }
  .card {
    position: relative;
    width: 1200px;
    height: 848px;
    background: var(--paper);
    color: var(--ink);
  }
  .swooshes {
    position: absolute;
    inset: 0;
  }
  .name {
    position: absolute;
    left: 128px;
    top: 150px;
    margin: 0;
    display: flex;
    align-items: flex-start;
    gap: 26px;
    font-weight: normal;
    white-space: nowrap;
  }
  .name-first {
    font-family: "Roboto", sans-serif;
    font-weight: 400;
    font-size: 172px;
    letter-spacing: 2px;
    line-height: 1;
  }
  .name-last {
    margin-top: 54px;
    font-family: "Open Sans", sans-serif;
    font-weight: 700;
    font-size: 46px;
    line-height: 1;
  }
  .portrait {
    position: absolute;
    left: 133px;
    top: 380px;
    width: 280px;
    height: 420px;
    background: linear-gradient(180deg, var(--portrait-top) 0%, var(--portrait-mid) 40%, var(--portrait-bottom) 100%);
  }
  .contact {
    position: absolute;
    left: 464px;
    top: 378px;
    width: 700px;
    margin: 0;
  }
  .contact-row {
    position: relative;
    height: 95px;
    white-space: nowrap;
  }
  .contact-label {
    position: absolute;
    left: 0;
    font-family: "Open Sans", sans-serif;
    font-size: 34px;
    text-decoration: underline wavy var(--wave);
    text-decoration-thickness: 1px;
    text-underline-offset: 6px;
  }
  .contact-value {
    position: absolute;
    left: 152px;
    margin: 0;
    font-family: "Roboto", sans-serif;
    font-weight: 300;
    line-height: 1;
  }
  .row-phone .contact-label { top: 0; }
  .row-phone .contact-value { top: 12px; font-size: 64px; }
  .row-email .contact-label { top: 6px; }
  .row-email .contact-value {
    top: 10px;
    font-family: "Roboto Condensed", sans-serif;
    font-size: 50px;
  }
  .row-skype .contact-label { top: 18px; }
  .row-skype .contact-value { top: 32px; font-size: 64px; }
</style>
</head>
<body>
<div class="card">
  <svg class="swooshes" width="1200" height="848" viewBox="0 0 1200 848" aria-hidden="true">
    <path fill="var(--swoosh-yellow)" d="M52 72 C 300 45, 700 40, 860 62 C 940 75, 1000 100, 1030 128 C 990 108, 920 92, 830 86 C 600 72, 300 80, 52 98 Z"/>
    <path fill="var(--swoosh-red)" d="M56 98 C 300 72, 650 60, 860 72 C 1000 82, 1100 110, 1148 134 C 1080 115, 980 100, 860 94 C 620 84, 320 96, 58 122 Z"/>
    <path fill="var(--swoosh-red)" d="M620 712 C 680 740, 760 760, 860 762 C 980 764, 1080 745, 1148 726 L 1148 748 C 1080 760, 980 772, 860 774 C 760 774, 680 752, 620 712 Z"/>
    <path fill="var(--swoosh-yellow)" d="M678 718 C 740 756, 820 778, 920 778 C 1020 778, 1100 762, 1150 750 L 1150 772 C 1090 786, 1010 794, 920 792 C 820 790, 730 766, 678 718 Z"/>
  </svg>

  <h1 class="name">
    <span class="name-first">Tomas</span><span class="name-last">VARLOW</span>
  </h1>

  <div class="portrait" role="img" aria-label="Portrait photograph of Tomas Varlow in a dark suit, leaning in an office"></div>

  <dl class="contact">
    <div class="contact-row row-phone">
      <dt class="contact-label">Phone:</dt>
      <dd class="contact-value">(917) 555-4173</dd>
    </div>
    <div class="contact-row row-email">
      <dt class="contact-label">Email:</dt>
      <dd class="contact-value">tomas@varlowcircle.example</dd>
    </div>
    <div class="contact-row row-skype">
      <dt class="contact-label">Skype::</dt>
      <dd class="contact-value">tomas.varlow</dd>
    </div>
  </dl>
</div>
</body>
</html>
```